Marwick Ostrand Law website for a law firm

modern clean website for a small boutique law firm. Based in Sacramento, CA and the Bay Area. Practice areas of Family Law, Civil litigation, and Criminal Defense. We already have a logo design as well as attorney pictures to include on page.
Would like images of California included on site.
Would like site to go with Logo that is already designed...blue/grey/white colors.

Industry/Entity Type

Law Firm

Number of Pages Required

5+ page

Requirements
Must have
• I already have several pages of content drafted. Just need the pages with images to input content. Must be clean and modern feel. Want it to reflect California and small boutique feel that is provided personalized legal attention.
• Must have a page where I can blog or post articles on.

```html
<!DOCTYPE html>
<html lang="en">
<head>
<meta charset="utf-8">
<title>Marwick Ostrand Law</title>
<link href="https://fonts.googleapis.com/css2?family=Open+Sans:wght@400;600&family=Questrial&display=swap" rel="stylesheet">
<style>
:root{
  --sky:#6a9ccb;
  --sky-light:#86b2d9;
  --brand-blue:#5393cc;
  --brand-grey:#8f9194;
  --nav-text:#3a3a3a;
  --card-bg:rgba(24,24,24,.9);
  --footer-bg:#1b1b1b;
  --footer-text:#d8d8d8;
  --white:#ffffff;
}
*{margin:0;padding:0;box-sizing:border-box}
html,body{width:1200px;height:844px;overflow:hidden}
body{position:relative;font-family:"Open Sans",sans-serif;background:var(--footer-bg);color:var(--white)}
.top-band{position:absolute;left:0;top:0;width:1200px;height:94px;background:linear-gradient(90deg,var(--sky-light),var(--sky) 60%,#5f93c4)}
.hero-photo{position:absolute;left:0;top:94px;width:1200px;height:582px;
  background:linear-gradient(90deg,#c9c6bf 0%,#dedad3 30%,#e7dfcf 55%,#d9c9a8 75%,#c8b48e 100%)}
.hero-photo::after{content:"";position:absolute;left:0;bottom:0;width:100%;height:110px;background:linear-gradient(180deg,rgba(150,150,150,0),rgba(120,120,120,.45))}
.logo-box{position:absolute;left:132px;top:15px;width:243px;height:107px;background:linear-gradient(#fff,#ececec);border-radius:4px 4px 0 0;box-shadow:0 3px 2px rgba(0,0,0,.25);z-index:2;display:flex;align-items:center;justify-content:center}
.brand-name{font-family:"Questrial",sans-serif;font-size:52px;color:var(--brand-grey);letter-spacing:1px;margin-top:10px}
.nav-bar{position:absolute;left:132px;top:64px;width:937px;height:58px;background:linear-gradient(#fff,#e9e9e9);box-shadow:0 3px 2px rgba(0,0,0,.25);border-radius:0 3px 3px 0}
.nav-bar ul{list-style:none;position:absolute;top:0;left:0;height:58px;width:100%}
.nav-bar li{position:absolute;top:18px;font-size:18px;color:var(--nav-text)}
.nav-bar li.active{color:var(--brand-blue)}
.nav-bar li svg{vertical-align:middle;margin-left:3px}
.phones{position:absolute;left:762px;top:15px;display:flex;align-items:center;gap:12px;font-size:18px;font-weight:600;color:var(--white)}
.card-icon{position:absolute;top:239px;width:76px;height:76px;background:var(--brand-blue);box-shadow:4px 4px 0 rgba(0,0,0,.22);display:flex;align-items:center;justify-content:center}
.card{position:absolute;top:324px;width:272px;height:238px;background:var(--card-bg);border-radius:22px;text-align:center;padding-top:18px}
.card h2{font-family:"Questrial",sans-serif;font-weight:400;font-size:29px;margin-bottom:10px}
.card p{font-size:16px;line-height:24.5px;padding:0 20px}
.card ul{list-style:none;font-size:18px;line-height:34px;margin-top:-4px}
.btn{position:absolute;left:50%;bottom:-16px;transform:translateX(-50%);width:129px;height:39px;border-radius:20px;background:var(--brand-blue);color:var(--white);font-size:18px;line-height:39px}
.footer-nav{position:absolute;left:0;width:1068px;top:703px;text-align:center;font-size:14.5px;color:var(--footer-text)}
.footer-nav span.sep{margin:0 12px;color:#888}
.footer-brand{position:absolute;left:134px;top:736px;font-family:"Questrial",sans-serif;font-size:38px;color:#777}
.social{position:absolute;left:492px;top:750px;display:flex;gap:10px}
.social span{width:15px;height:15px;border-radius:50%;background:var(--footer-text)}
.copyright{position:absolute;left:0;width:1068px;top:793px;text-align:center;font-size:14.5px;color:var(--footer-text)}
.subscribe{position:absolute;left:778px;top:738px;width:291px;height:44px}
.sub-icon{position:absolute;left:0;top:0;width:44px;height:44px;border-radius:50%;background:var(--brand-blue);border:2px solid #dfe7f0;display:flex;align-items:center;justify-content:center;z-index:1}
.sub-input{position:absolute;left:40px;top:9px;width:155px;height:24px;border:1px solid #666;background:#1e1e1e;color:#999;font-size:12px;line-height:22px;text-align:center}
.sub-btn{position:absolute;left:203px;top:6px;width:88px;height:31px;background:#333;color:var(--white);font-size:14.5px;line-height:31px;text-align:center;border-radius:2px}
</style>
</head>
<body>
<div class="top-band"></div>
<div class="hero-photo" role="img" aria-label="Photo of a courthouse column beside brass scales of justice on a desk"></div>

<header>
  <div class="nav-bar">
    <ul>
      <li class="active" style="left:439px">Home</li>
      <li style="left:530px">About Us<svg width="11" height="8" viewBox="0 0 11 8"><path d="M1 1l4.5 5L10 1" fill="none" stroke="#3a3a3a" stroke-width="1.5"/></svg></li>
      <li style="left:656px">Practice Areas<svg width="11" height="8" viewBox="0 0 11 8"><path d="M1 1l4.5 5L10 1" fill="none" stroke="#3a3a3a" stroke-width="1.5"/></svg></li>
      <li style="left:818px">Contact Us</li>
    </ul>
  </div>
  <div class="logo-box"><span class="brand-name">MOLAW</span></div>
  <div class="phones">
    <svg width="34" height="34" viewBox="0 0 34 34"><circle cx="17" cy="17" r="15.5" fill="none" stroke="#fff" stroke-width="2"/><path d="M13 9c-2 1-3 3-2 7s4 8 7 9c2 0 3-1 3-2l-2-3-2 1c-1-1-3-4-3-6l2-1-1-4z" fill="#fff"/></svg>
    <span>(916) 555-0142&nbsp;&nbsp;/&nbsp;&nbsp;(925) 555-0187</span>
  </div>
</header>

<main>
  <div class="card-icon" style="left:230px">
    <svg width="40" height="36" viewBox="0 0 40 36" fill="#fff"><path d="M20 0L2 8h36z"/><rect x="4" y="10" width="32" height="3"/><rect x="7" y="15" width="4" height="12"/><rect x="14" y="15" width="4" height="12"/><rect x="22" y="15" width="4" height="12"/><rect x="29" y="15" width="4" height="12"/><rect x="3" y="29" width="34" height="3"/><rect x="0" y="33" width="40" height="3"/></svg>
  </div>
  <section class="card" style="left:132px">
    <h2>About Us</h2>
    <p>After practicing in both the private and public sector for several years, Clara Marwick and Anders Ostrand joined their legal expertise and formed...</p>
    <a class="btn">Read More</a>
  </section>

  <div class="card-icon" style="left:564px">
    <svg width="42" height="36" viewBox="0 0 42 36" fill="none" stroke="#fff" stroke-width="2.5"><path d="M4 6l17-3 17-3M21 3v30M13 34h16"/><path d="M8 6l-6 14h12zM34 3l-6 14h12z"/><path d="M2 20a6 5 0 0012 0M28 17a6 5 0 0012 0" fill="#fff"/></svg>
  </div>
  <section class="card" style="left:466px">
    <h2>Practice Areas</h2>
    <ul><li>- Business Law</li><li>- Real Estate Law</li><li>- Criminal Law</li></ul>
    <a class="btn">View All</a>
  </section>

  <div class="card-icon" style="left:895px">
    <svg width="40" height="38" viewBox="0 0 40 38" fill="none" stroke="#fff" stroke-width="2.5"><path d="M3 3h34v32H3z"/><path d="M8 10h24M8 16h10v12H8zM22 16h10M22 21h10M22 26h10"/></svg>
  </div>
  <section class="card" style="left:797px">
    <h2>News</h2>
    <p>Lorem Ipsum is simply dummy text of the printing and typesetting industry. Lorem Ipsum has been the industry’s standard dummy text...</p>
    <a class="btn">View All</a>
  </section>
</main>

<footer>
  <nav class="footer-nav">Home<span class="sep">|</span>About Us<span class="sep">|</span>Practice Areas<span class="sep">|</span>Contact Us</nav>
  <div class="footer-brand">MOLAW</div>
  <div class="social" aria-label="Social links"><span></span><span></span><span></span><span></span></div>
  <div class="copyright">Copyright © 2017 MOLAW</div>
  <div class="subscribe">
    <div class="sub-icon"><svg width="20" height="18" viewBox="0 0 20 18" fill="#fff"><rect x="4" y="0" width="12" height="9" opacity=".8"/><path d="M0 9h6l2 3h4l2-3h6v9H0z"/></svg></div>
    <div class="sub-input">Enter Your Email</div>
    <div class="sub-btn">Subscribe</div>
  </div>
</footer>
</body>
</html>
```